Law Firm Needs Brochure Redesign Using New Logo

We are a personal injury law firm that does auto injuries and other personal injury cases. We want a new brochure that has our updated logo and information. Instead of gold and black, we want more navy, as matches the new logo. The Auto Liability portion should read: "(required by the state of Arizona in the amounts of $25,000 per person / $50,000 per accident, but a higher amount may be best )." The other information can remain the same. We'd like the brochure to keep the same professional tone as the previous brochure.
Our website is https://www.brandtlegalpartners.example/.

```html
<!DOCTYPE html>
<html lang="en">
<head>
<meta charset="utf-8">
<title>Brandt Law – Protect Your Family Brochure</title>
<link href="https://fonts.googleapis.com/css2?family=Roboto+Condensed:wght@400;700;800&family=Open+Sans:wght@400;600;700&display=swap" rel="stylesheet">
<style>
:root{
  --page:#d9dbdf;
  --navy:#0c2550;
  --navy-deep:#081a3a;
  --blue:#1e6fd6;
  --blue-light:#7fb4ff;
  --ink:#1b2a44;
  --muted:#5b6678;
  --white:#ffffff;
  --rule:rgba(255,255,255,.28);
}
*{box-sizing:border-box;margin:0;padding:0}
html,body{width:1200px;height:3372px;overflow:hidden}
body{background:var(--page);font-family:"Open Sans",sans-serif;color:var(--ink);position:relative}
.spread{position:absolute;left:20px;width:1160px;height:1000px;display:grid;grid-template-columns:repeat(3,1fr);box-shadow:0 10px 30px rgba(0,0,0,.25);background:var(--white)}
.spread--outside{top:620px}
.spread--inside{top:1740px}
.panel{position:relative;overflow:hidden}
.panel--navy{background:linear-gradient(180deg,var(--navy) 0%,var(--navy-deep) 100%);color:var(--white)}
.cond{font-family:"Roboto Condensed",sans-serif}

/* brand */
.brand{font-family:"Roboto Condensed",sans-serif;font-weight:800;letter-spacing:1px;color:var(--navy);display:flex;align-items:center;gap:10px}
.brand__mark{width:14px;height:14px;background:var(--blue)}

/* stats panel */
.stats{padding:70px 44px 0}
.stat__over{font-family:"Roboto Condensed",sans-serif;font-size:26px;letter-spacing:1px}
.stat__num{font-family:"Roboto Condensed",sans-serif;font-weight:800;font-size:72px;line-height:1;color:var(--blue-light)}
.stat__text{font-size:17px;line-height:1.45;margin-top:10px;color:#d8e4f7}
.stat{border-top:2px solid var(--rule);padding:20px 0 26px}
.stat:first-child{border-top:0}
.stats__body{font-size:15px;line-height:1.6;color:#c7d5ec;margin-top:6px}
.phone{position:absolute;left:44px;bottom:42px;display:flex;align-items:center;gap:12px;font-family:"Roboto Condensed",sans-serif;font-weight:700;font-size:30px;color:var(--white)}

/* contact panel */
.contact{padding:70px 40px 0;text-align:center}
.contact__title{font-family:"Roboto Condensed",sans-serif;font-weight:800;font-size:28px;color:var(--navy);letter-spacing:1px}
.contact__lines{font-size:15px;line-height:1.6;color:var(--muted);margin-top:14px}
.contact .brand{justify-content:center;font-size:32px;margin-top:70px}
.photo-circle{width:240px;height:240px;border-radius:50%;margin:56px auto 0;border:8px solid var(--navy);background:radial-gradient(circle at 50% 55%,#c8353a 0 22%,#e7ecf3 40%,#9fb4d0 100%)}
.web-band{position:absolute;left:0;right:0;bottom:0;height:70px;background:var(--navy);color:var(--white);display:flex;align-items:center;justify-content:center;font-family:"Roboto Condensed",sans-serif;font-weight:700;font-size:18px;letter-spacing:1px}
.diag{position:absolute;top:0;right:0}

/* cover */
.cover__top{padding:60px 36px 0}
.cover .brand{font-size:30px}
.headline{font-family:"Roboto Condensed",sans-serif;font-weight:800;line-height:.95;color:var(--navy);margin-top:36px}
.headline__sm{font-size:44px;display:block}
.headline__lg{font-size:86px;display:block}
.headline__accent{font-size:44px;display:block;color:var(--blue)}
.tagline{font-size:15px;color:var(--muted);margin-top:14px}
.cover__photo{position:absolute;left:0;right:0;bottom:0;height:470px;background:linear-gradient(160deg,#1c2b45 0%,#0b1630 60%,#0d4b8f 100%)}
.cover__slice{position:absolute;left:0;bottom:0}

/* tips */
.tips{padding:60px 36px 0}
.tips__title{font-family:"Roboto Condensed",sans-serif;font-weight:800;font-size:50px;line-height:1}
.tips__sub{font-family:"Roboto Condensed",sans-serif;font-weight:800;font-size:34px;color:var(--blue-light);margin-top:4px}
.tips__list{list-style:none;margin-top:26px}
.tips__item{display:flex;gap:12px;font-size:12.5px;line-height:1.45;color:#d3def2;margin-bottom:12px}
.tips__num{flex:0 0 24px;height:24px;border-radius:50%;background:var(--blue);color:var(--white);font-weight:700;font-size:12px;display:flex;align-items:center;justify-content:center}

/* coverage */
.coverage__head{background:var(--navy);color:var(--white);font-family:"Roboto Condensed",sans-serif;font-weight:800;font-size:26px;text-align:center;padding:22px 10px;margin:40px 0 0}
.coverage__head em{font-style:normal;color:var(--blue-light)}
.coverage__intro{font-size:14px;line-height:1.5;color:var(--muted);padding:18px 32px 8px;text-align:center}
.coverage__item{display:flex;gap:12px;padding:10px 32px}
.coverage__icon{flex:0 0 28px;height:28px;background:var(--blue);border-radius:4px}
.coverage__name{font-weight:700;color:var(--blue);font-size:14px}
.coverage__text{font-size:12.5px;line-height:1.45;color:var(--muted)}
.coverage__photo{position:absolute;left:0;right:0;bottom:0;height:230px;background:linear-gradient(135deg,#f2f4f8 0%,#c9d3e3 55%,#b8323a 100%)}

/* safety */
.safety{padding:60px 40px 0;text-align:center}
.safety__title{font-family:"Roboto Condensed",sans-serif;font-weight:800;font-size:38px;line-height:1.05}
.safety__title span{display:block;color:var(--blue-light)}
.safety__text{font-size:14px;line-height:1.55;color:#d3def2;margin:12px 0 40px}
.safety__photo{position:absolute;left:0;right:0;bottom:0;height:420px;background:linear-gradient(160deg,#6b6f78 0%,#2b2f38 60%,#15181f 100%)}
</style>
</head>
<body>

<section class="spread spread--outside">
  <div class="panel panel--navy">
    <div class="stats">
      <div class="stat">
        <div class="stat__over">OVER</div>
        <div class="stat__num">107,000</div>
        <p class="stat__text">crashes will happen in the state of Arizona this year.</p>
      </div>
      <div class="stat">
        <div class="stat__over">OVER</div>
        <div class="stat__num">700</div>
        <p class="stat__text">of them will result in fatalities.</p>
      </div>
      <p class="stats__body">If we don't win, you don't pay attorney fees. That seems fair to us. Know what's happening with your case, get the answers to your questions and work on getting better with the confidence that you've got an excellent group of people working for you.</p>
    </div>
    <div class="phone">
      <svg width="26" height="26" viewBox="0 0 24 24" fill="#ffffff"><path d="M6.6 10.8a15.1 15.1 0 0 0 6.6 6.6l2.2-2.2a1 1 0 0 1 1-.25 11.4 11.4 0 0 0 3.6.57 1 1 0 0 1 1 1V20a1 1 0 0 1-1 1A17 17 0 0 1 3 4a1 1 0 0 1 1-1h3.5a1 1 0 0 1 1 1c0 1.25.2 2.45.57 3.57a1 1 0 0 1-.25 1z"/></svg>
      602.555.0147
    </div>
  </div>

  <div class="panel contact">
    <svg class="diag" width="120" height="300" viewBox="0 0 120 300"><polygon points="120,0 60,0 120,300" fill="#1e6fd6"/><polygon points="120,0 100,0 120,120" fill="#0c2550"/></svg>
    <h2 class="contact__title">CONTACT US</h2>
    <p class="contact__lines">Brandt Legal Partners<br>4410 N. Cedar Avenue Suite 210<br>Phoenix AZ 85016<br>602.555.0147<br>info@brandtlegalpartners.example<br>brandtlegalpartners.example</p>
    <div class="brand"><span class="brand__mark"></span>BRANDT LAW</div>
    <div class="photo-circle" role="img" aria-label="Photo of a red car with a hand holding it, in a circular frame"></div>
    <div class="web-band">WWW.BRANDTLEGALPARTNERS.EXAMPLE</div>
  </div>

  <div class="panel cover">
    <div class="cover__top">
      <div class="brand"><span class="brand__mark"></span>BRANDT LAW</div>
      <h1 class="headline">
        <span class="headline__sm">PROTECT YOUR</span>
        <span class="headline__lg">FAMILY</span>
        <span class="headline__sm">IN CASE OF</span>
        <span class="headline__accent">A CAR ACCIDENT</span>
      </h1>
      <p class="tagline">A little knowledge and preparation go a long way</p>
    </div>
    <div class="cover__photo" role="img" aria-label="Photo of a man in a suit holding his hands around a glowing car icon"></div>
    <svg class="cover__slice" width="387" height="470" viewBox="0 0 387 470"><polygon points="0,0 90,0 0,200" fill="#1e6fd6"/><polygon points="0,0 387,0 387,14 0,14" fill="#0c2550"/></svg>
  </div>
</section>

<section class="spread spread--inside">
  <div class="panel panel--navy">
    <div class="tips">
      <h2 class="tips__title">TOP 10 TIPS</h2>
      <div class="tips__sub">TO AVOID A CRASH</div>
      <ol class="tips__list">
        <li class="tips__item"><span class="tips__num">1</span>Before turning left, wait until the way is fully clear and never rush the gap.</li>
        <li class="tips__item"><span class="tips__num">2</span>When your light turns green, pause a moment and check for drivers running the red.</li>
        <li class="tips__item"><span class="tips__num">3</span>Leave plenty of room between you and the car in front, more at night or in rain.</li>
        <li class="tips__item"><span class="tips__num">4</span>Avoid driving drowsy. Pull over and rest if your eyes feel heavy.</li>
        <li class="tips__item"><span class="tips__num">5</span>Keep the radio and phone set before you go so your hands stay on the wheel.</li>
        <li class="tips__item"><span class="tips__num">6</span>Watch mirrors often and check blind spots before every lane change.</li>
        <li class="tips__item"><span class="tips__num">7</span>Be extra careful on weekends and late nights when impaired drivers are out.</li>
        <li class="tips__item"><span class="tips__num">8</span>Slow down in work zones and school zones and watch for people on foot.</li>
        <li class="tips__item"><span class="tips__num">9</span>Never drink and drive. Plan a ride home before the evening starts.</li>
        <li class="tips__item"><span class="tips__num">10</span>Keep your tires, brakes and lights in good shape with regular checks.</li>
      </ol>
    </div>
    <div class="phone">
      <svg width="26" height="26" viewBox="0 0 24 24" fill="#ffffff"><path d="M6.6 10.8a15.1 15.1 0 0 0 6.6 6.6l2.2-2.2a1 1 0 0 1 1-.25 11.4 11.4 0 0 0 3.6.57 1 1 0 0 1 1 1V20a1 1 0 0 1-1 1A17 17 0 0 1 3 4a1 1 0 0 1 1-1h3.5a1 1 0 0 1 1 1c0 1.25.2 2.45.57 3.57a1 1 0 0 1-.25 1z"/></svg>
      602.555.0147
    </div>
  </div>

  <div class="panel coverage">
    <h2 class="coverage__head">HAVE THE <em>RIGHT</em> COVERAGE</h2>
    <p class="coverage__intro">Many people don't know about the different kinds of insurance available in addition to health insurance. We suggest:</p>
    <div class="coverage__item"><span class="coverage__icon"></span><div><div class="coverage__name">Auto Liability</div><p class="coverage__text">(required by the state of Arizona in the amounts of $25,000 per person / $50,000 per accident, but a higher amount may be best).</p></div></div>
    <div class="coverage__item"><span class="coverage__icon"></span><div><div class="coverage__name">Uninsured or Underinsured Motorist Coverage</div><p class="coverage__text">This protects you when the other driver has no insurance or not enough to cover your losses.</p></div></div>
    <div class="coverage__item"><span class="coverage__icon"></span><div><div class="coverage__name">Medical Payments Coverage</div><p class="coverage__text">Helps pay medical bills for you and your passengers no matter who is at fault in a crash.</p></div></div>
    <div class="coverage__item"><span class="coverage__icon"></span><div><div class="coverage__name">Comprehensive / Rental Insurance</div><p class="coverage__text">Protects you in case of damage to your car and keeps you moving while it is repaired.</p></div></div>
    <div class="coverage__photo" role="img" aria-label="Photo of hands cupped protectively around a small red toy car"></div>
  </div>

  <div class="panel panel--navy">
    <div class="safety">
      <h2 class="safety__title">MODEL SAFE <span>BEHAVIOR</span></h2>
      <p class="safety__text">Always buckle up. Always put your children in car seats or boosters that are right for their height and weight.</p>
      <h2 class="safety__title">NEVER TEXT <span>WHILE DRIVING</span></h2>
      <p class="safety__text">Studies have shown that texting while driving is as dangerous as driving intoxicated. Show your children that no text is more important than their safety.</p>
    </div>
    <div class="safety__photo" role="img" aria-label="Close-up photo of a hand fastening a car seat belt"></div>
  </div>
</section>

</body>
</html>
```